Brindle Offers is an online marketing platform.

A daily deals site for consumers a way to bring in new clients for clients and this is who the business cards are for. Industries - Food and Drink, Things To Do, Beauty and Spas, Staycations and Services.
Logo on one side.
Name - Owen Radley
Job Title - Sales Director
Phone Number - 07912358046
Email - owen@brindleoffers.co.uk
need same for second person
Name - Fiona Bracken
Job Title - Operations Director
Phone Number - 01632840275
Email - fiona@brindleoffers.co.uk
Bottom Right - Chatterbook Icon, Snapa Icon, Pipline Icon
Target Market(s)
Business owners of the above industries
Contact Information for Business Card
Name - Owen Radley
Name - Fiona Bracken
Look and feel

```html
<!DOCTYPE html>
<html lang="en">
<head>
<meta charset="utf-8">
<title>Brindle Offers – Business Cards</title>
<link rel="stylesheet" href="https://fonts.googleapis.com/css2?family=Mulish:wght@400;600;800&display=swap">
<style>
  :root {
    --brand-blue: #1456b8;
    --brand-blue-dark: #0f4aa3;
    --card-white: #ffffff;
    --backdrop: #2b2e33;
    --handle-blue: #1a5fc4;
    --dot-navy: #1d3a7a;
    --dot-sky: #2f8ee0;
    --dot-amber: #e8803a;
  }
  * { box-sizing: border-box; margin: 0; padding: 0; }
  html, body {
    width: 1200px; height: 900px; overflow: hidden;
    background: var(--backdrop);
    font-family: "Mulish", sans-serif;
  }
  .canvas { position: relative; width: 1200px; height: 900px; }

  .card {
    position: absolute;
    background: var(--card-white);
    box-shadow: 0 12px 30px rgba(0,0,0,.35);
  }
  .card--landscape { left: 90px; top: 310px; width: 500px; height: 286px; }
  .card--portrait-back { left: 650px; top: 230px; width: 240px; height: 420px; background: linear-gradient(160deg, var(--brand-blue), var(--brand-blue-dark)); }
  .card--portrait-front { left: 920px; top: 230px; width: 240px; height: 420px; }

  .wordmark {
    position: absolute; left: 50%; transform: translateX(-50%);
    display: flex; align-items: center; gap: 8px;
    white-space: nowrap;
    font-weight: 800; color: var(--brand-blue);
  }
  .wordmark__dot { border-radius: 50%; background: var(--brand-blue); flex: none; }

  .card--landscape .wordmark { top: 122px; font-size: 30px; }
  .card--landscape .wordmark__dot { width: 18px; height: 18px; }

  .card--portrait-front .wordmark { top: 160px; font-size: 22px; }
  .card--portrait-front .wordmark__dot { width: 14px; height: 14px; }

  .social {
    position: absolute; left: 50%; bottom: 60px; transform: translateX(-50%);
    display: flex; align-items: center; gap: 4px; white-space: nowrap;
  }
  .social__dot { width: 11px; height: 11px; border-radius: 50%; }
  .social__dot--chatterbook { background: var(--dot-navy); }
  .social__dot--pipline { background: var(--dot-sky); }
  .social__dot--snapa { background: var(--dot-amber); }
  .social__handle { margin-left: 6px; font-size: 11px; color: var(--handle-blue); letter-spacing: .04em; }

  .contact { position: absolute; left: 60px; top: 52px; color: #fff; }
  .contact__name { font-size: 17px; font-weight: 800; letter-spacing: .02em; }
  .contact__role { font-size: 9px; opacity: .85; margin-top: 3px; margin-bottom: 10px; }
  .contact__line { display: flex; align-items: center; gap: 7px; font-size: 9.5px; letter-spacing: .06em; margin-top: 5px; white-space: nowrap; }
  .contact__icon { width: 9px; height: 9px; flex: none; }
</style>
</head>
<body>
<main class="canvas">

  <section class="card card--landscape" aria-label="Business card front">
    <div class="wordmark"><span class="wordmark__dot"></span>Brindle Offers</div>
  </section>

  <section class="card card--portrait-back" aria-label="Business card contact side">
    <div class="contact">
      <div class="contact__name">Owen Radley</div>
      <div class="contact__role">Sales Director</div>
      <div class="contact__line">
        <svg class="contact__icon" viewBox="0 0 10 10" aria-hidden="true"><rect x="2.5" y="0.5" width="5" height="9" rx="1" fill="none" stroke="#fff" stroke-width="1"/><line x1="4.2" y1="8" x2="5.8" y2="8" stroke="#fff" stroke-width="0.8"/></svg>
        07912358046
      </div>
      <div class="contact__line">
        <svg class="contact__icon" viewBox="0 0 10 10" aria-hidden="true"><rect x="0.5" y="2" width="9" height="6" fill="#fff"/><polyline points="0.5,2 5,5.5 9.5,2" fill="none" stroke="#1456b8" stroke-width="0.9"/></svg>
        owen@brindleoffers.co.uk
      </div>
    </div>
  </section>

  <section class="card card--portrait-front" aria-label="Business card logo side">
    <div class="wordmark"><span class="wordmark__dot"></span>Brindle Offers</div>
    <div class="social">
      <span class="social__dot social__dot--chatterbook" aria-label="Chatterbook"></span>
      <span class="social__dot social__dot--pipline" aria-label="Pipline"></span>
      <span class="social__dot social__dot--snapa" aria-label="Snapa"></span>
      <span class="social__handle">brindleoffers</span>
    </div>
  </section>

</main>
</body>
</html>
```